Law Firm Stationery Design - Traditional Meets Intuitive

Looking for a modern, yet classic, law firm stationery design. Simplicity is desired, but great ideas are encouraged. See attachment for company information. We utilize a variety of non-traditional legal tools to bring a different perspective to each of our client's particular situation. Final design should communicate classic values with intuitive, unique solutions.

Industry/Entity Type

Law Firm

Requirements
Should not have
• - No typical legal icons
• - No Tag Line!
• - DO NOT WANT WHAT WE ALREADY HAVE

```html
<!DOCTYPE html>
<html lang="en">
<head>
<meta charset="utf-8">
<title>Veritan Law – Business Card</title>
<link rel="stylesheet" href="https://fonts.googleapis.com/css2?family=Gelasio:wght@400&family=Arimo:wght@400;700&display=swap">
<style>
  :root {
    --backdrop: #3a3634;
    --card: #141517;
    --card-edge: #1d1f22;
    --silver: #8d9094;
    --silver-dim: #6b6e72;
    --white: #f4f4f4;
    --blue: #1f7fc4;
    --divider: #5a5d61;
  }
  * { box-sizing: border-box; margin: 0; padding: 0; }
  html, body {
    width: 1200px; height: 864px; overflow: hidden;
    background: var(--backdrop);
  }
  .stage {
    width: 1200px; height: 864px;
    display: flex; flex-direction: column;
    align-items: center; justify-content: center; gap: 40px;
  }
  .card {
    width: 660px; height: 377px;
    background: linear-gradient(135deg, var(--card-edge), var(--card));
    position: relative;
  }
  .wordmark {
    font-family: "Gelasio", Georgia, serif;
    font-weight: 400; line-height: 1; white-space: nowrap;
  }

  /* Front */
  .card-front .wordmark {
    position: absolute; left: 160px; top: 118px;
    font-size: 64px; color: var(--silver);
  }
  .card-front .site {
    position: absolute; left: 172px; top: 248px;
    font-family: "Arimo", Arial, sans-serif; font-size: 14px;
    letter-spacing: 0.42em; color: var(--silver-dim); white-space: nowrap;
  }

  /* Back */
  .card-back .wordmark {
    position: absolute; left: 44px; top: 166px;
    font-size: 44px; color: var(--white);
  }
  .card-back .divider {
    position: absolute; left: 338px; top: 92px; width: 1px; height: 196px;
    background: linear-gradient(to bottom, transparent, var(--divider) 20%, var(--divider) 80%, transparent);
  }
  .details {
    position: absolute; left: 364px; top: 100px;
    font-family: "Arimo", Arial, sans-serif; color: var(--white); white-space: nowrap;
  }
  .person-name {
    font-size: 18px; font-weight: 700; color: var(--blue); letter-spacing: 0.02em;
  }
  .person-role { font-size: 15px; margin-top: 2px; }
  .address { font-size: 14px; line-height: 1.35; margin-top: 14px; }
  .contacts { list-style: none; margin-top: 12px; font-size: 14px; }
  .contacts li { display: flex; align-items: center; gap: 8px; height: 22px; }
  .contacts svg { width: 14px; height: 14px; flex: none; }
</style>
</head>
<body>
<main class="stage">
  <section class="card card-front" aria-label="Card front">
    <div class="wordmark">Veritan Law</div>
    <div class="site">www.veritanlaw.com</div>
  </section>

  <section class="card card-back" aria-label="Card back">
    <div class="wordmark">Veritan Law</div>
    <div class="divider"></div>
    <div class="details">
      <div class="person-name">MARK ELLERY</div>
      <div class="person-role">President</div>
      <div class="address">
        VERITAN LAW LLC<br>
        18 Harbor Lane, Suite 300<br>
        Dalton, MA 01226
      </div>
      <ul class="contacts">
        <li>
          <svg viewBox="0 0 14 14" aria-hidden="true"><rect x="3" y="0.5" width="8" height="13" rx="1.5" fill="none" stroke="var(--blue)" stroke-width="1.4"/><rect x="5.5" y="10.5" width="3" height="1.2" fill="var(--blue)"/></svg>
          555-014-2200
        </li>
        <li>
          <svg viewBox="0 0 14 14" aria-hidden="true"><rect x="0.5" y="2.5" width="13" height="9" fill="var(--blue)"/><path d="M0.5 2.5 L7 8 L13.5 2.5" fill="none" stroke="var(--card)" stroke-width="1.2"/></svg>
          info@veritanlaw.com
        </li>
        <li>
          <svg viewBox="0 0 14 14" aria-hidden="true"><circle cx="7" cy="7" r="6.5" fill="var(--blue)"/><path d="M0.5 7 H13.5 M7 0.5 C4 4 4 10 7 13.5 M7 0.5 C10 4 10 10 7 13.5" fill="none" stroke="var(--card)" stroke-width="1"/></svg>
          www.veritanlaw.com
        </li>
      </ul>
    </div>
  </section>
</main>
</body>
</html>
```